BRV Coffee bag (front and back)

We use black matte bags and have front and back labels. We have a logo but need an attractive and inviting label. The labels will be used for our entire line of coffees. We sell most of our coffee to foodservice establishments (Restaurants, Hotels, Bakeries, Bodegas) and we would like to have these establishments display our bags of coffee to sell retail.
The logo can be used as a whole or using any one of the three components (Logo, image, tag).

Target Market(s)

People who buy the coffee they brew at home from the local shop they get their morning latte.. We are a local coffee company, but we do not sell locally roasted coffee!

Industry/Entity Type

Food

Font styles to use
Other font styles liked:
• something that looks good with our trademarked BRV

Colors

Designer to choose colors to be used in the design.

Requirements
Must have
• Respect Trademarked logo
Nice to have
• It would be nice to have a design that can be used with other mediums (airpot wraps, java jackets, )
Should not have
• Real People

```html
<!DOCTYPE html>
<html lang="en">
<head>
<meta charset="utf-8">
<title>BRV Coffee – Back Label</title>
<link href="https://fonts.googleapis.com/css2?family=Montserrat:ital,wght@0,400;0,500;0,700;1,400;1,500&display=swap" rel="stylesheet">
<style>
  :root {
    --page: #ffffff;
    --label: #000000;
    --gold: #c8965c;
    --gold-light: #e2b57e;
    --text: #d9a56a;
    --faint: #3c3c3c;
  }
  * { box-sizing: border-box; margin: 0; padding: 0; }
  html, body { width: 1200px; height: 909px; overflow: hidden; background: var(--page); }
  body { position: relative; font-family: "Montserrat", sans-serif; }

  .back-label {
    position: absolute; left: 410px; top: 163px;
    width: 380px; height: 582px;
    background: var(--label); border-radius: 4px; overflow: hidden;
  }
  .label-frame {
    position: absolute; inset: 10px;
    border: 1.5px solid var(--gold);
  }
  .brand-watermark {
    position: absolute; left: -20px; top: 170px;
    font-family: "Montserrat", sans-serif; font-weight: 700;
    font-size: 170px; line-height: 1; color: var(--faint);
    letter-spacing: -4px;
  }
  .section-title {
    position: absolute; left: 0; width: 100%; text-align: center;
    font-weight: 700; font-size: 19px; letter-spacing: 0.5px; color: var(--gold);
  }
  .title-rule { position: absolute; left: 50%; transform: translateX(-50%); }
  .step-list { position: absolute; left: 94px; list-style: none; }
  .step {
    position: relative; padding-left: 18px; margin-bottom: 14px;
    font-style: italic; font-size: 11.5px; line-height: 14px; color: var(--text);
  }
  .step-bullet { position: absolute; left: 0; top: 2px; width: 8px; height: 10px; }
  .divider { position: absolute; left: 50%; top: 421px; transform: translateX(-50%); }
  .distributor {
    position: absolute; left: 60px; top: 460px;
    font-size: 11.5px; line-height: 15px; color: var(--text);
  }
</style>
</head>
<body>
<svg width="0" height="0" style="position:absolute">
  <defs>
    <linearGradient id="gold-taper" x1="0" x2="1">
      <stop offset="0" stop-color="#c8965c" stop-opacity="0"/>
      <stop offset="0.5" stop-color="#e2b57e"/>
      <stop offset="1" stop-color="#c8965c" stop-opacity="0"/>
    </linearGradient>
    <symbol id="bean" viewBox="0 0 8 10">
      <ellipse cx="4" cy="5" rx="3.4" ry="4.6" transform="rotate(25 4 5)" fill="#c8965c"/>
      <path d="M3 1.5 Q5 5 4.5 8.5" stroke="#000" stroke-width="0.8" fill="none"/>
    </symbol>
  </defs>
</svg>

<section class="back-label">
  <div class="brand-watermark">BRV</div>
  <div class="label-frame"></div>

  <h2 class="section-title" style="top:84px">BREWING</h2>
  <svg class="title-rule" style="top:110px" width="120" height="5"><path d="M0 2.5 L60 0.5 L120 2.5 L60 4.5 Z" fill="url(#gold-taper)"/></svg>
  <ul class="step-list" style="top:140px">
    <li class="step"><svg class="step-bullet"><use href="#bean"/></svg>Use fresh filtered cold water.</li>
    <li class="step"><svg class="step-bullet"><use href="#bean"/></svg>Measure 2 TBSP of coffee<br>for every 6 oz water.</li>
    <li class="step"><svg class="step-bullet"><use href="#bean"/></svg>Brew with water 195°F-205°F.</li>
  </ul>

  <h2 class="section-title" style="top:280px">STORING</h2>
  <svg class="title-rule" style="top:306px" width="120" height="5"><path d="M0 2.5 L60 0.5 L120 2.5 L60 4.5 Z" fill="url(#gold-taper)"/></svg>
  <ul class="step-list" style="top:334px">
    <li class="step"><svg class="step-bullet"><use href="#bean"/></svg>Store in an airtight container<br>in a cool , dry place.</li>
    <li class="step"><svg class="step-bullet"><use href="#bean"/></svg>Do not freeze.</li>
  </ul>

  <svg class="divider" width="240" height="5"><path d="M0 2.5 L120 0.5 L240 2.5 L120 4.5 Z" fill="url(#gold-taper)"/></svg>

  <address class="distributor" style="font-style:normal">
    Distributed by:<br>
    BRV Coffee Company, LLC.<br>
    info@brvcoffee.example<br>
    555.267-0100
  </address>
</section>
</body>
</html>
```